Wine Shop Banners

Banner graphic/images required
Require banner images to match the present online wine shop.

www.kelterhaus-traube.de

The wine-shop presently has a very clean, simple design, lots of white space, which is very much the trend at the moment.

Requirements
Images or graphic design for present banners visible on the homepage

The colour and feeling of the banners must fit in with the present clean, simple design.

Work required
3 large slide-card/banners (can be more) and 3 smaller fixed banners below. Please view website to see present position of banners.

LARGE BANNERS x 3

Something special with white background within the banner space
White background on each slide-card. Small individual graphic image in the middle of the slide card. This could be either a simple element of wine:
ingredients, fruit (grape), bottle, cork, old bottle label etc. just displaying one item on each slide-card. Preferably with high quality graphic features.

Note:
We are trying the steer away from the classic stereotype wineshop design. The image/s should have a higher, individual graphic touch, which gives the design something different. Sometimes such artistic work is displayed in steampunk or even in nostalgic design, which leaves the viewer slightly memorized with the content.
To clarify: we are not looking for a full steampunk design but possibly certain elements of this will give you an idea what we mean. That is to say, the design can go slightly in this direction without going over the top. Something small but very eye-catching.

SMALLER BANNERS x 3

One idea is:
Showing a symbol e.g. - discount sign "%" against a white background but again with a high graphic quality.

Target Market(s)

People interested in purchasing wine.
Ages approx. 25 to 65

Industry/Entity Type

Shop

Requirements
Must have
• Something special with white background
• Small individual graphic image in the middle of the slide card.
Nice to have
• The image/s should have a higher, individual graphic touch, which gives the design something different. Something that leaves the viewer slightly memorized with the content.
Should not have
• Not the typical classical design that is often seen on wine shops.

```html
<!DOCTYPE html>
<html lang="de">
<head>
<meta charset="utf-8">
<title>Kelterhaus Traube – Weinshop</title>
<link href="https://fonts.googleapis.com/css2?family=Exo+2:wght@300;400;500&family=Libre+Baskerville:ital@0;1&family=Allura&family=Cormorant+Garamond:ital,wght@1,400;1,500&display=swap" rel="stylesheet">
<style>
:root{
  --olive:#5a6432;
  --crimson:#b0234a;
  --lime:#cfdb63;
  --lime-text:#c4d25a;
  --text:#555;
  --muted:#9a9a9a;
  --line:#d9d9d9;
  --tan:#c8b99b;
  --brown:#7b6a58;
  --wine:#5a0f12;
}
*{box-sizing:border-box;margin:0;padding:0}
html,body{width:1200px;height:748px;overflow:hidden;background:#fff}
body{position:relative;font-family:"Exo 2",sans-serif;font-weight:300;color:var(--text)}
.abs{position:absolute}

.brand{left:34px;top:34px;width:170px}
.brand-name{font-family:"Exo 2",sans-serif;font-weight:500;font-size:27px;color:var(--olive);letter-spacing:1px;line-height:1;display:flex;align-items:center;gap:8px}
.brand-dot{width:12px;height:12px;border-radius:50%;background:var(--olive);display:inline-block}
.brand-sub{font-family:"Exo 2",sans-serif;font-weight:500;font-size:27px;color:var(--olive);letter-spacing:1px;line-height:1.2;padding-left:20px}

.search{left:592px;top:52px;width:314px;height:36px;border:1px solid #9a9a9a;display:flex}
.search-field{flex:1;display:flex;align-items:center;gap:14px;padding-left:12px;font-size:15px;color:#666}
.search-go{width:46px;background:var(--crimson);color:#fff;font-size:16px;display:flex;align-items:center;justify-content:center;font-weight:400}

.account{left:1011px;top:40px;display:flex;align-items:center;gap:16px;font-size:18px;color:#666}

.nav{left:52px;top:136px;display:flex;font-size:18px;color:#666}
.nav span{margin-right:40px}

.badge{position:absolute;top:-8px;right:-8px;width:19px;height:19px;border-radius:50%;background:#b8c12a;color:#fff;font-size:11px;font-weight:400;display:flex;align-items:center;justify-content:center}

.filter-head{left:33px;top:180px;width:233px;height:40px;background:var(--lime);color:#4a4a4a;font-weight:500;font-size:16px;padding:9px 13px}
.group-title{left:36px;font-size:16px;font-weight:400;color:var(--lime-text)}
.facets{left:36px;list-style:none;font-size:16px;color:#555}
.facets li{height:25px;display:flex;align-items:center;gap:9px}
.facets li::before{content:"›";font-size:16px;color:#555}
.facets em{font-style:normal;color:var(--muted)}
.scroll-list{top:266px;height:182px;overflow:hidden}
.scrollbar{left:250px;top:266px;width:14px;height:182px;background:#f0f0f0;border:1px solid #e2e2e2}
.scrollbar i{position:absolute;left:2px;top:12px;width:8px;height:82px;background:#c8c8c8}

.hero{left:279px;top:179px;width:867px;height:341px;background:#fff;box-shadow:0 0 6px rgba(0,0,0,.12);overflow:hidden}
.hero-title{position:absolute;left:78px;top:70px;font-family:"Allura",cursive;color:var(--wine);font-size:78px;line-height:.85}
.hero-title span{display:block;padding-left:46px}
.hero-visual{position:absolute;left:470px;top:0;width:397px;height:341px;background:radial-gradient(ellipse at 50% 55%,#4a3a36 0%,#2a1e1e 40%,#cfc4b0 62%,#fff 80%)}
.dots{position:absolute;right:16px;bottom:22px;display:flex;gap:14px}
.dots i{width:17px;height:17px;border-radius:50%;background:#fff;display:block;box-shadow:0 0 2px rgba(0,0,0,.3)}

.promo{top:529px;width:282px;height:134px;overflow:hidden;background:linear-gradient(90deg,#f3f3f3,#d8d8d8)}
.promo-shape{position:absolute;inset:0;clip-path:polygon(105px 134px,180px 0,282px 0,282px 134px)}
.promo-copy{position:absolute;font-family:"Cormorant Garamond",serif;font-style:italic;color:#6b5d4e;line-height:1.15}
.promo-big{position:absolute;font-family:"Cormorant Garamond",serif;font-style:italic;color:#fff;line-height:1}
.play{position:absolute;right:8px;bottom:8px}
.splash{position:absolute;left:0;top:0;width:190px;height:134px;background:linear-gradient(135deg,#e7e3dc,#b8ad9e 50%,#ece9e4)}

.featured{left:277px;top:686px;display:flex;align-items:center;gap:10px;font-family:"Libre Baskerville",serif;font-size:17px;color:#333}
.pager{top:686px;width:19px;height:20px;border:1px solid #777;display:flex;align-items:center;justify-content:center}
.card{top:720px;width:216px;height:40px;border:1px solid #eee;border-bottom:none;box-shadow:0 -2px 3px rgba(0,0,0,.06)}
</style>
</head>
<body>

<div class="abs brand">
  <div class="brand-name"><i class="brand-dot"></i>Kelterhaus</div>
  <div class="brand-sub" style="font-size:14px;letter-spacing:4px;padding-left:0;margin-top:6px">TRAUBE · WEIN SHOP</div>
</div>

<div class="abs search">
  <div class="search-field">
    <svg width="15" height="15" viewBox="0 0 15 15"><circle cx="6" cy="6" r="4.5" fill="none" stroke="#b0234a" stroke-width="2"/><line x1="9.5" y1="9.5" x2="13.5" y2="13.5" stroke="#b0234a" stroke-width="2.2"/></svg>
    Suche
  </div>
  <div class="search-go">GO</div>
</div>

<div class="abs account">Abmelden
  <svg width="26" height="32" viewBox="0 0 26 32"><circle cx="13" cy="9" r="6.5" fill="none" stroke="#777" stroke-width="1.8"/><path d="M2 30v-5a6 6 0 0 1 6-6h10a6 6 0 0 1 6 6v5z" fill="none" stroke="#777" stroke-width="1.8"/></svg>
</div>

<nav class="abs nav"><span>Rotwein</span><span>Weißwein</span><span>Rosewein</span><span>Sekt / Champagner</span><span>Sonderangebote</span><span>Probierpakete</span></nav>

<div class="abs" style="left:1047px;top:133px;width:30px;height:28px">
  <svg width="30" height="28" viewBox="0 0 30 28"><path d="M1 3h5l4 15h14l3-10H8" fill="none" stroke="#777" stroke-width="2"/><circle cx="12" cy="24" r="2.2" fill="#777"/><circle cx="22" cy="24" r="2.2" fill="#777"/></svg>
  <span class="badge">0</span>
</div>
<div class="abs" style="left:1106px;top:130px;width:34px;height:34px;border-radius:50%;background:#8a8a8a">
  <svg width="34" height="34" viewBox="0 0 34 34"><path d="M17 24l-7-7a4 4 0 0 1 7-5 4 4 0 0 1 7 5z" fill="none" stroke="#fff" stroke-width="1.8"/></svg>
  <span class="badge">0</span>
</div>

<div class="abs filter-head">DETAILSUCHE</div>

<div class="abs group-title" style="top:236px">LAND</div>
<ul class="abs facets scroll-list">
  <li>Italien <em>(87)</em></li><li>Frankreich <em>(74)</em></li><li>Deutschland <em>(58)</em></li><li>Spanien <em>(35)</em></li><li>Südafrika <em>(15)</em></li><li>Österreich <em>(12)</em></li><li>Australien <em>(12)</em></li><li>Portugal <em>(10)</em></li>
</ul>
<div class="abs scrollbar"><i></i></div>

<div class="abs group-title" style="top:472px">GESCHMACK</div>
<ul class="abs facets" style="top:503px">
  <li>Trocken <em>(303)</em></li><li>Halbtrocken <em>(8)</em></li><li>Lieblich <em>(5)</em></li><li>Süß <em>(3)</em></li><li>Edelsüss <em>(1)</em></li>
</ul>

<div class="abs group-title" style="top:651px">FARBE</div>
<ul class="abs facets" style="top:682px">
  <li>Rot <em>(155)</em></li><li>Weiß <em>(127)</em></li>
</ul>

<section class="abs hero">
  <div class="hero-title">Select<span>Reserve</span></div>
  <div class="hero-visual" role="img" aria-label="Foto: Rotweinglas vor einer Korbflasche und einer liegenden Rotweinflasche"></div>
  <div class="dots"><i></i><i></i><i></i></div>
</section>

<div class="abs promo" style="left:278px">
  <div class="promo-shape" style="background:var(--tan)"></div>
  <div class="promo-copy" style="left:26px;top:24px;font-size:25px">free shipping<br>on orders<br>over</div>
  <div class="promo-big" style="left:160px;top:42px;font-size:68px">$25</div>
  <svg class="play" width="22" height="22" viewBox="0 0 22 22"><circle cx="11" cy="11" r="10" fill="#fff"/><path d="M8.5 6.5l6 4.5-6 4.5z" fill="var(--tan)"/></svg>
</div>

<div class="abs promo" style="left:571px">
  <div class="splash" role="img" aria-label="Foto: Weinkorken mit Spritzern"></div>
  <div class="promo-shape" style="background:var(--brown)"></div>
  <div class="promo-big" style="left:154px;top:50px;font-size:33px;line-height:.85">celebrate<br>in style</div>
  <svg class="play" width="22" height="22" viewBox="0 0 22 22"><circle cx="11" cy="11" r="10" fill="#fff"/><path d="M8.5 6.5l6 4.5-6 4.5z" fill="var(--brown)"/></svg>
</div>

<div class="abs promo" style="left:864px">
  <div class="promo-shape" style="background:var(--brown);clip-path:polygon(105px 134px,170px 0,282px 0,282px 134px)"></div>
  <div class="promo-copy" style="left:26px;top:40px;font-size:38px;line-height:.85;color:#7b6a58">special<br>offers</div>
  <div class="promo-big" style="left:170px;top:22px;font-size:22px">save up to</div>
  <div class="promo-big" style="left:148px;top:50px;font-size:64px">35%</div>
  <svg class="play" width="22" height="22" viewBox="0 0 22 22"><circle cx="11" cy="11" r="10" fill="#fff"/><path d="M8.5 6.5l6 4.5-6 4.5z" fill="var(--brown)"/></svg>
</div>

<div class="abs featured">
  <svg width="20" height="20" viewBox="0 0 20 20"><circle cx="10" cy="10" r="8.5" fill="none" stroke="var(--crimson)" stroke-width="1.5"/><path d="M8 6l5 4-5 4z" fill="var(--crimson)"/></svg>
  Ausgewählte Produkte
</div>
<div class="abs pager" style="left:1102px"><svg width="8" height="12" viewBox="0 0 8 12"><path d="M6 1L2 6l4 5" fill="none" stroke="#555" stroke-width="1.4"/></svg></div>
<div class="abs pager" style="left:1126px"><svg width="8" height="12" viewBox="0 0 8 12"><path d="M2 1l4 5-4 5" fill="none" stroke="#555" stroke-width="1.4"/></svg></div>

<div class="abs card" style="left:274px"></div>
<div class="abs card" style="left:494px"></div>
<div class="abs card" style="left:714px"></div>
<div class="abs card" style="left:934px"></div>

</body>
</html>
```